Business card for event manager / organizer "velmora tandem"

Draft of a new valuable business card for my company.
Events, personnel service providers, festivals

```html
<!DOCTYPE html>
<html lang="de">
<head>
<meta charset="utf-8">
<title>velmora tandem – Visitenkarte</title>
<link href="https://fonts.googleapis.com/css2?family=Lato:wght@400;700;900&display=swap" rel="stylesheet">
<style>
  :root {
    --bg: #e9e7e4;
    --paper: #ffffff;
    --ink: #1b1b1b;
    --orange: #f07f1e;
    --grey: #7a7a7a;
    --dark-card: #2a2a2c;
    --silver: #c9c9cb;
    --edge: #b8632a;
  }
  * { box-sizing: border-box; margin: 0; padding: 0; }
  html, body { width: 1200px; height: 675px; overflow: hidden; }
  body {
    background: var(--bg);
    font-family: "Lato", Arial, sans-serif;
    position: relative;
  }
  .card {
    position: absolute;
    top: 162px;
    width: 540px;
    height: 350px;
    border-radius: 4px;
    box-shadow: 0 6px 18px rgba(0,0,0,.18);
    overflow: hidden;
  }
  .card--front { left: 40px; background: var(--paper); }
  .card--back { left: 620px; background: var(--dark-card); border-bottom: 4px solid var(--edge); }

  .portrait {
    position: absolute;
    right: 0; top: 0;
    width: 265px; height: 350px;
    background: linear-gradient(180deg, #f4f1ee 0%, #e8dcd4 35%, #d8434a 62%, #f1efed 100%);
  }

  .brand {
    position: absolute;
    left: 26px; top: 92px;
    display: flex; align-items: center; gap: 10px;
  }
  .brand__mark {
    width: 30px; height: 30px;
    background: var(--orange);
  }
  .brand__name {
    font-weight: 900;
    font-size: 28px;
    color: var(--ink);
    letter-spacing: .5px;
    line-height: 1;
  }
  .brand__claim {
    position: absolute;
    left: 66px; top: 130px;
    font-size: 10px;
    color: var(--ink);
  }

  .person { position: absolute; left: 26px; top: 170px; }
  .person__name { color: var(--orange); font-size: 20px; font-weight: 400; letter-spacing: .5px; }
  .person__role { color: var(--grey); font-size: 13px; margin-top: 2px; }

  .contact {
    position: absolute; left: 26px; top: 222px;
    list-style: none;
  }
  .contact li {
    display: flex; align-items: center; gap: 9px;
    font-size: 13.5px; color: var(--grey);
    line-height: 19px;
  }
  .contact svg { width: 12px; height: 12px; flex: none; fill: var(--orange); stroke: var(--orange); }

  .back-logo {
    position: absolute; left: 0; right: 0; top: 128px;
    display: flex; justify-content: center; align-items: center; gap: 14px;
  }
  .back-logo__mark {
    width: 44px; height: 44px;
    border: 2px solid var(--silver);
  }
  .back-logo__name {
    font-weight: 900; font-size: 40px;
    color: var(--silver); letter-spacing: 1px;
  }
  .back-claim {
    position: absolute; left: 0; right: 0; top: 192px;
    text-align: center; font-size: 12px; color: var(--silver);
  }
</style>
</head>
<body>

<section class="card card--front">
  <div class="portrait" role="img" aria-label="Foto: lächelnder Kellner mit roter Weste und Fliege hält einen Stapel weißer Teller"></div>

  <div class="brand">
    <span class="brand__mark"></span>
    <span class="brand__name">velmora tandem</span>
  </div>
  <p class="brand__claim">…denn die nächste Feier kommt bestimmt!</p>

  <div class="person">
    <p class="person__name">LENA HARTWIG</p>
    <p class="person__role">Inhaberin</p>
  </div>

  <ul class="contact">
    <li>
      <svg viewBox="0 0 12 12"><path d="M2.5 1l2 2-1 1.5c.6 1.4 1.6 2.4 3 3L8 6.5l2 2-1.2 1.8C5 10 2 7 1.7 3.2z" stroke="none"/></svg>
      021 40 512 73 18
    </li>
    <li>
      <svg viewBox="0 0 12 12"><rect x="3" y="1" width="6" height="10" rx="1" fill="none" stroke-width="1.2"/></svg>
      0160 284 37 92
    </li>
    <li>
      <svg viewBox="0 0 12 12"><circle cx="6" cy="6" r="5.5" stroke="none"/></svg>
      /velmoratandem
    </li>
    <li>
      <svg viewBox="0 0 12 12"><rect x="1" y="2.5" width="10" height="7" fill="none" stroke-width="1.2"/><path d="M1 2.5l5 4 5-4" fill="none" stroke-width="1.2"/></svg>
      info@velmora-tandem.de
    </li>
    <li>
      <svg viewBox="0 0 12 12"><circle cx="6" cy="6" r="5" fill="none" stroke-width="1.1"/><ellipse cx="6" cy="6" rx="2.2" ry="5" fill="none" stroke-width="1"/><path d="M1 6h10" fill="none" stroke-width="1"/></svg>
      www.velmora-tandem.de
    </li>
    <li>
      <svg viewBox="0 0 12 12"><path d="M6 11.5S2 7 2 4.5a4 4 0 018 0C10 7 6 11.5 6 11.5z" stroke="none"/><circle cx="6" cy="4.5" r="1.4" fill="#fff" stroke="none"/></svg>
      Lindenweg 14, 48155 Musterstadt
    </li>
  </ul>
</section>

<section class="card card--back">
  <div class="back-logo">
    <span class="back-logo__mark"></span>
    <span class="back-logo__name">velmora tandem</span>
  </div>
  <p class="back-claim">…denn die nächste Feier kommt bestimmt!</p>
</section>

</body>
</html>
```